Guiding Resilient Artistry through Calm Emotional Training

FLYER FOR MENTAL SKILLS TRAINING AND CHOREOGRAPHY
For more information please see attachment.
For more information please see attachment
Thank you..

Target Market(s)

athletes, dancers and choreographers

Industry/Entity Type

Training

Font styles to use
Serif

Colors
32a5d7
0392cd
85cae6

Requirements
Must have
• email address: gracebymiralovane@mailnova.net
• phone number: (555) 231-7809
• PageWave: www.pagewave.net/movementbymiralovane
Nice to have
• Everything that is in the file I have attached. Flattering and eye catching unisex color. Logo should be included on the very first page.

```html
<!DOCTYPE html>
<html lang="en">
<head>
<meta charset="utf-8">
<title>Make The Right Call… Join GRACE!</title>
<link rel="stylesheet" href="https://fonts.googleapis.com/css2?family=Cinzel:wght@900&family=Kalam:wght@700&family=PT+Serif:wght@400;700&family=Ubuntu:wght@700&family=Roboto+Slab:wght@400&display=swap">
<style>
  :root {
    --navy-deep: #141a3c;
    --navy: #1f2a55;
    --sky: #32a5d7;
    --sky-bright: #0392cd;
    --sky-soft: #85cae6;
    --ink: #1b1b1b;
    --white: #ffffff;
    --panel-top: #fdf0b8;
    --panel-bottom: #f9b548;
    --panel-edge: #f0a23a;
    --question-red: #8c1d1d;
    --heading-blue: #1f4f9e;
    --side-top: #f9b48c;
    --side-bottom: #f5895a;
    --table-line: #2b2b2b;
  }
  html, body {
    margin: 0;
    padding: 0;
    width: 884px;
    height: 1200px;
    overflow: hidden;
  }
  .flyer {
    position: relative;
    width: 884px;
    height: 1200px;
    background: linear-gradient(180deg, var(--navy-deep) 0%, var(--navy) 100%);
    overflow: hidden;
    font-family: "PT Serif", serif;
  }
  .headline {
    position: absolute;
    left: 108px;
    top: 62px;
    margin: 0;
    color: var(--white);
    font-family: "Cinzel", serif;
    font-weight: 900;
    font-size: 52px;
    line-height: 62px;
    letter-spacing: 1px;
  }
  .headline em {
    font-style: italic;
    text-decoration: underline;
    text-decoration-thickness: 4px;
    text-underline-offset: 6px;
  }
  .logo-block {
    position: absolute;
    left: 113px;
    top: 289px;
    width: 506px;
    height: 314px;
    background: var(--sky);
  }
  .logo-figure {
    position: absolute;
    left: 0;
    top: 0;
    width: 150px;
    height: 314px;
    background: linear-gradient(180deg, var(--sky) 0%, var(--sky-bright) 100%);
  }
  .logo-acronym {
    position: absolute;
    left: 110px;
    top: 52px;
    margin: 0;
    padding: 0;
    list-style: none;
    color: var(--ink);
    font-family: "PT Serif", serif;
    font-size: 27px;
    line-height: 48px;
  }
  .questions {
    position: absolute;
    left: 43px;
    top: 625px;
    width: 728px;
    height: 239px;
    box-sizing: border-box;
    border: 3px solid var(--panel-edge);
    border-radius: 26px;
    background: linear-gradient(180deg, var(--panel-top) 0%, var(--panel-bottom) 100%);
    padding: 24px 40px 0 60px;
  }
  .questions ol {
    margin: 0;
    padding-left: 30px;
    color: var(--question-red);
    font-family: "Roboto Slab", serif;
    font-size: 17.5px;
    line-height: 30px;
  }
  .offer {
    position: absolute;
    left: 43px;
    top: 886px;
    width: 728px;
    height: 280px;
    box-sizing: border-box;
    border: 3px solid var(--panel-edge);
    border-radius: 26px;
    background: linear-gradient(180deg, var(--panel-top) 0%, var(--panel-bottom) 100%);
  }
  .offer-heading {
    margin: 16px 30px 0;
    text-align: center;
    color: var(--heading-blue);
    font-family: "Ubuntu", sans-serif;
    font-weight: 700;
    font-size: 20px;
    line-height: 28px;
  }
  .price-table {
    position: absolute;
    border-collapse: collapse;
    border: 2px solid var(--table-line);
  }
  .price-table td {
    border: 2px solid var(--table-line);
    padding: 2px 6px;
    vertical-align: top;
  }
  .price-table--sessions { left: 14px; top: 94px; width: 374px; }
  .price-table--routines { left: 392px; top: 116px; width: 318px; }
  .service {
    font-family: "Kalam", cursive;
    font-weight: 700;
    font-size: 21px;
    line-height: 22px;
    color: var(--ink);
    text-align: center;
  }
  .price-table--routines .service { text-align: left; }
  .rate {
    font-family: "PT Serif", serif;
    font-variant: small-caps;
    font-size: 17px;
    line-height: 18px;
    color: var(--ink);
  }
  .price-table--sessions tr { height: 58px; }
  .price-table--routines tr:first-child { height: 92px; }
  .price-table--routines tr:last-child { height: 58px; }
  .contact-strip {
    position: absolute;
    left: 787px;
    top: 356px;
    width: 85px;
    height: 830px;
    box-sizing: border-box;
    border-radius: 14px;
    background: linear-gradient(180deg, var(--side-top) 0%, var(--side-bottom) 100%);
    padding: 38px 5px 0 8px;
    color: var(--white);
    font-family: "Ubuntu", sans-serif;
    font-size: 13.5px;
    line-height: 22px;
    overflow-wrap: anywhere;
  }
  .contact-strip p { margin: 0; }
</style>
</head>
<body>
  <main class="flyer">
    <h1 class="headline">Make The <em>Right</em><br>Call… Join<br>GRACE!</h1>

    <section class="logo-block" aria-label="GRACE">
      <div class="logo-figure" role="img" aria-label="Dark silhouette of a dancer with arms outstretched"></div>
      <ul class="logo-acronym">
        <li>Guiding Resilient Artistry</li>
        <li>through</li>
        <li>Calm</li>
        <li>Emotional</li>
        <li>Training</li>
      </ul>
    </section>

    <section class="questions">
      <ol>
        <li>Consider all athletic successes that you've had. What percentage of time were you mentally focused?</li>
        <li>Consider your athletic performance. What percentage of mistakes were considered to be mental errors?</li>
        <li>Consider your preparation. What percentage of time do you spend on mental training?</li>
      </ol>
    </section>

    <section class="offer">
      <h2 class="offer-heading">We have a lot of different workshops and types of sessions to offer!</h2>
      <table class="price-table price-table--sessions">
        <tr><td class="service">Team Workshops</td><td class="rate">$250 per contact/hour</td></tr>
        <tr><td class="service">Coach Workshops</td><td class="rate">$250 per contact/hour</td></tr>
        <tr><td class="service">Individual Sessions</td><td class="rate">$100 per contact hour</td></tr>
      </table>
      <table class="price-table price-table--routines">
        <tr><td class="service">Floor Routines/ Beam Routines</td><td class="rate">$400 per gymnast<br>$150 per gymnast</td></tr>
        <tr><td class="service">Dance Lessons</td><td class="rate">$25 per contact hour</td></tr>
      </table>
    </section>

    <aside class="contact-strip">
      <p>If you are interested in any of those workshops or sessions feel free to contact us by email: gracebymiralovane@mailnova.net or by phone: (555) 231-7809 or check out more info on PageWave, at www.pagewave.net/movementbymiralovane.</p>
    </aside>
  </main>
</body>
</html>
```